International sports trophy business needs a web design

We need two pages designed for a new company called medalnook. We sell innovative sports trophies via our website and store details of past purchases to allow returning customers to easily place their orders. Customers can log into their accounts using chatterlane or a secondary account login button. The final design should be clean and should focus on the theme of winning the trophy as it is applicable to all sports.

The page should be designed with themes that can be used throughout the site that we'll turn into a cms theme.
Updates

Hi All,

We're half way in to the competition now and I thought it'd be a good time to provide an update on how things are progressing.  First let me thank you for taking part, there's some really great ideas happening here however some of you have requested a mockup for the second page.  I've put that up now and you should be able to find it in the files section of the brief.  Hopefully this will give people a better starting point than before.

To everybody who is still waiting for feedback, be patient, I'm currently working my way through the designs and will be in contact shortly.  I thought in the meantime I could provide a general update as to how I think the competition is progressing and the concepts that I like the most so far. 

For the landing page... The designs that are leading at the moment are not busy or crowded and devote most of the page layout to the front page info-graphic.  The logo, login and primary menu are all easy to identify but not where your eye lands when viewing the page.  The copyright information and secondary menus are there if you look for them.  As far as the style goes we've found that some of the designs feel a little too serious and too adult and we'd like a more playful feel, if you think that your design already is playful, then we probably do too.  Finally I'll add that we like our logo, but that doesn't mean that we want to see it more than once on the landing page (it's pointless and designs that do this will be unlikely to win) and we certainly do not want to see people creating a new logo or changing our name to nook medal.

For the trophy sales page... There are fewer designs done to this specification as some are unwilling to invest the time in design or unwilling to work without a mockup.  The mockup has now been uploaded to the site (we did want to see what kind of ideas would come here if we didn't include one, thanks to those who had a shot).  If you have any other query about the sales page feel free to contact us.

A final general comment, we want to make sure that all of the images used in your designs are not infringing copyright (this includes images in our mockups, we can only guarantee that we own the copyright for the medalnook logo.).

Hi all, the sliders below have been updated to reflect the more playful design feel that we prefer so far.

Target Market(s)

Our target market is sporting and youth focused but must be adult friendly.

Industry/Entity Type

Business

Requirements
Must have
• We want two pages designed, a landing page and a product display page. We would like a common border scheme across both showing the logo (attached) in the top corner, and secondary links along the bottom.

Landing Page - Must Haves

We see trophies as a representation of achievement and something that can be shared with friends and family. We would like to convey this message in a graphic or illustration on the landing page. Currently in the mockup we have a bunch of trophies, this should not be the final image here.

We have attached a wireframe for the basic format that we'd like to see, you're free to expand upon this as you see fit.

Product Display Page - Must Haves

The product display page will feature a coverflow type device that holds images of the available trophies. It should show the category of the trophy, in this case choose a specific sport to feature (up to you). There should be space for the details of the trophy including price, dimensions, product name, product code, material. There should be room on the page for advertising, this will be common throughout the site except for the landing page. You should include buttons to allow you to add the trophy to your shopping cart and a shopping cart graphic somewhere on the page. There should be a menu bar, unique to this page, that allows a user to choose a new trophy to buy, view previous purchases, view current cart and account settings.

Should not have
• The design should be sport neutral, so don't focus on a single sport or category of sports or sports particular to a certain nationality. With that it's probably easier to just focus on the trophy and achievement aspect rather than the sport being played.

```html
<!DOCTYPE html>
<html lang="en">
<head>
<meta charset="utf-8">
<title>medalnook — Sports Trophies</title>
<link href="https://fonts.googleapis.com/css2?family=Archivo+Black&family=Arimo:wght@400;700&family=Kameron:wght@400;700&display=swap" rel="stylesheet">
<style>
  :root {
    --page-bg: #ffffff;
    --panel-bg: #ececf0;
    --panel-border: #dcdce2;
    --ink-dark: #4a4a4a;
    --ink-body: #8a8a8a;
    --ink-soft: #6f6f6f;
    --accent-red: #c4242f;
    --accent-maroon: #8a1530;
    --nav-bg: #e2e2e6;
    --nav-active: #d2d2d8;
    --nav-border: #b9b9bf;
    --gold-light: #d9b15a;
    --gold-dark: #7a561c;
    --icon-orange: #e8852a;
    --icon-green: #7cb53a;
    --icon-blue: #3b6cb4;
  }
  * { box-sizing: border-box; margin: 0; padding: 0; }
  html, body { width: 1200px; height: 884px; overflow: hidden; background: var(--page-bg); }
  body { position: relative; font-family: "Arimo", Arial, sans-serif; color: var(--ink-dark); }

  .brand { position: absolute; left: 167px; top: 42px; display: flex; align-items: center; gap: 10px; }
  .brand-mark { width: 22px; height: 22px; border-radius: 50%; background: var(--accent-maroon); }
  .brand-name { font-family: "Arimo", sans-serif; font-weight: 700; font-size: 28px; letter-spacing: 2px; color: #222; }

  .social-login { position: absolute; left: 969px; top: 0; width: 64px; height: 25px; background: linear-gradient(#fff, #e8e8ec); border: 1px solid #c8c8cf; border-top: none; border-radius: 0 0 4px 4px; box-shadow: 0 2px 3px rgba(0,0,0,.2); display: flex; align-items: center; justify-content: center; gap: 5px; font-size: 11px; font-weight: 700; color: #333; }
  .social-login .dot { width: 13px; height: 13px; border-radius: 50%; background: var(--icon-blue); }

  .account-links { position: absolute; right: 168px; top: 33px; display: flex; align-items: center; gap: 14px; font-size: 11px; font-weight: 700; color: #333; }
  .account-links span { display: flex; align-items: center; gap: 7px; }
  .account-links svg { width: 18px; height: 18px; }

  .main-nav { position: absolute; left: 699px; top: 60px; width: 333px; height: 35px; display: flex; border: 1px solid var(--nav-border); border-radius: 4px; background: linear-gradient(#ededf0, var(--nav-bg)); overflow: hidden; }
  .main-nav a { flex: 1; display: flex; align-items: center; justify-content: center; text-decoration: none; font-size: 14px; font-weight: 700; color: #7a7a7a; border-left: 1px solid var(--nav-border); }
  .main-nav a:first-child { border-left: none; color: var(--accent-maroon); background: var(--nav-active); }

  .hero { position: absolute; left: 167px; top: 101px; width: 865px; height: 499px; background: var(--panel-bg); border: 1px solid var(--panel-border); border-radius: 5px; }
  .hero-visual { position: absolute; left: 60px; top: 22px; width: 293px; height: 450px; border-radius: 10px; background: radial-gradient(ellipse at 45% 40%, var(--gold-light), #a97a2c 60%, var(--gold-dark)); opacity: .85; }
  .hero-copy { position: absolute; left: 409px; top: 136px; width: 405px; }
  .hero-title { font-family: "Archivo Black", sans-serif; font-size: 21.5px; color: #444; letter-spacing: .5px; margin-bottom: 9px; }
  .hero-text { font-family: "Kameron", serif; font-size: 14.5px; line-height: 25.5px; color: var(--ink-body); }
  .btn-readmore { display: inline-block; margin-top: 10px; width: 113px; height: 24px; line-height: 24px; text-align: center; font-size: 13px; color: #888; background: linear-gradient(#fff, #e9e9ec); box-shadow: 2px 2px 3px rgba(0,0,0,.25); }

  .feature { position: absolute; top: 623px; width: 276px; height: 165px; background: linear-gradient(#ddddE3, #f4f4f6); border: 1px solid var(--panel-border); border-radius: 5px; }
  .feature.who { left: 167px; }
  .feature.what { left: 461px; }
  .feature.news { left: 756px; }
  .feature h2 { position: absolute; left: 19px; top: 16px; font-size: 14px; font-weight: 700; color: var(--accent-red); }
  .feature p { position: absolute; left: 19px; top: 36px; width: 150px; font-size: 11.5px; line-height: 18.5px; color: var(--ink-body); white-space: nowrap; }
  .feature .more { position: absolute; left: 19px; top: 137px; font-size: 10.5px; color: var(--ink-body); display: flex; align-items: center; gap: 6px; }
  .feature .more::before { content: ""; width: 6px; height: 6px; background: var(--accent-red); }
  .feature-icon { position: absolute; right: 12px; top: 24px; width: 88px; height: 88px; border-radius: 14px; }
  .who .feature-icon { border-radius: 50%; background: radial-gradient(circle at 40% 35%, #fff, #c9c9cc 55%, #8a8a90); }
  .what .feature-icon { background: radial-gradient(circle, #d23a3a, #7e1717 70%, #3a3a3e); }
  .news .feature-icon { background: linear-gradient(135deg, #fafafa 55%, #e8305a); }

  .site-footer { position: absolute; left: 167px; top: 801px; width: 865px; height: 26px; border-top: 1px solid #e6e6e8; border-bottom: 1px solid #e6e6e8; display: flex; align-items: center; justify-content: space-between; padding: 0 10px; font-size: 10.5px; color: #666; }
  .footer-links span.sep { margin: 0 12px; }
  .footer-right { display: flex; align-items: center; gap: 7px; }
  .follow-icon { width: 14px; height: 14px; border-radius: 2px; }
  .follow-icon.a { background: #5ab0d8; }
  .follow-icon.b { background: #2a6aa8; }
  .follow-icon.c { background: #e8782a; }
  .follow-icon.d { background: #3b5a98; }
</style>
</head>
<body>
  <header>
    <div class="brand"><span class="brand-mark"></span><span class="brand-name">medalnook</span></div>
    <div class="social-login"><span class="dot"></span>Login</div>
    <div class="account-links">
      <span><svg viewBox="0 0 18 18"><rect width="18" height="18" rx="3" fill="#e8852a"/><circle cx="8" cy="8" r="3.5" fill="none" stroke="#fff" stroke-width="2"/><line x1="10.5" y1="10.5" x2="14" y2="14" stroke="#fff" stroke-width="2"/></svg>Register</span>
      <span><svg viewBox="0 0 18 18"><rect x="1" y="3" width="16" height="12" fill="#fff" stroke="#888"/><circle cx="6" cy="8" r="2" fill="#888"/><line x1="10" y1="7" x2="15" y2="7" stroke="#888"/><line x1="10" y1="10" x2="15" y2="10" stroke="#888"/></svg>My Account</span>
      <span><svg viewBox="0 0 18 18"><circle cx="9" cy="9" r="8" fill="#7cb53a"/><path d="M9 4v7M6 8l3 3 3-3" stroke="#fff" stroke-width="2" fill="none"/></svg>Login</span>
    </div>
    <nav class="main-nav">
      <a href="#">HOME</a><a href="#">WHAT ?</a><a href="#">WHY ?</a><a href="#">TOUR</a>
    </nav>
  </header>

  <main>
    <section class="hero">
      <div class="hero-visual" role="img" aria-label="Golden football trophy with a player striking an overhead kick on a star-decorated base"></div>
      <div class="hero-copy">
        <h1 class="hero-title">LOREM IPSUM DOLOR SIT</h1>
        <p class="hero-text">Lorem Ipsum is simply dummy text of the printing and typeset­ting industry. Lorem Ipsum has been the industry's standard dummy text ever since the 1500s, when an unknown printer took a galley of type and scrambled it to make a type specimen book...</p>
        <span class="btn-readmore">Readmore</span>
      </div>
    </section>

    <section class="feature who">
      <h2>WHO WE ARE ?</h2>
      <p>Lorem Ipsum is simply<br>dummy text of the printing<br>and typesetting industry.<br>Lorem Ipsum has been the<br>industry's standard dummy</p>
      <div class="feature-icon" role="img" aria-label="Glossy silver globe with red network lines"></div>
      <span class="more">Read more</span>
    </section>
    <section class="feature what">
      <h2>WHAT WE DO ?</h2>
      <p>Lorem Ipsum is simply<br>dummy text of the printing<br>and typesetting industry.<br>Lorem Ipsum has been the<br>industry's standard dummy</p>
      <div class="feature-icon" role="img" aria-label="Red app-style tile with a silver gear"></div>
      <span class="more">Read more</span>
    </section>
    <section class="feature news">
      <h2>NEWS</h2>
      <p>Lorem Ipsum is simply<br>dummy text of the printing<br>and typesetting industry.<br>Lorem Ipsum has been the<br>industry's standard dummy</p>
      <div class="feature-icon" role="img" aria-label="Paper sheet with a fountain pen over a pink card"></div>
      <span class="more">Read more</span>
    </section>
  </main>

  <footer class="site-footer">
    <div class="footer-links">Sitemap<span class="sep">|</span>Contact<span class="sep">|</span>FAQ<span class="sep">|</span>Terms of Use<span class="sep">|</span>Privacy Policy</div>
    <div class="footer-right">Copyright © 2011 medalnook. All rights reserved. Follow us on
      <span class="follow-icon a"></span><span class="follow-icon b"></span><span class="follow-icon c"></span><span class="follow-icon d"></span>
    </div>
  </footer>
</body>
</html>
```